Online Course Page

We are building a video based online course page. This project is for only the actual page that the student will watch the videos at. They will watch one vide at a time. Once one video lesson is completed then they can move to the next video lesson. The page will need to show the video player. (Main feature.) The list of lessons in the course. Instructor information. Profile picture and bio of the instructor. A Live chat button that will initiate a chat in real-time with the instructor.

The winning designer will also be asked to to design the dashboard area and other aspects of the user interface as an additional project.

Target Market(s)

Adults

Number of Pages Required

1 page

Colors
9bcb3c

Requirements
Must have
• Our logo is attached. Green and grey are our colors. Should feel modern, clean and be simple to navigate. The site will be responsive so the layout should work well on mobile devices.

```html
<!DOCTYPE html>
<html lang="en">
<head>
<meta charset="utf-8">
<title>Course Lesson Page</title>
<link href="https://fonts.googleapis.com/css2?family=Open+Sans:wght@300;400;600;700&display=swap" rel="stylesheet">
<style>
:root{
  --green:#8cc63f;
  --green-bright:#9bcb3c;
  --ink:#333;
  --text:#555;
  --muted:#8a8a8a;
  --line:#e3e3e3;
  --side:#f8f8f8;
  --side-top:#f2f2f2;
  --bubble-grey:#ececec;
  --white:#fff;
}
*{box-sizing:border-box;margin:0;padding:0}
html,body{width:1200px;height:953px;overflow:hidden;background:var(--white);font-family:"Open Sans",Arial,sans-serif;color:var(--ink)}
.abs{position:absolute}
.header{position:absolute;left:0;top:0;width:1200px;height:70px;background:var(--white);box-shadow:0 1px 4px rgba(0,0,0,.06);z-index:2}
.brand{position:absolute;left:31px;top:22px;display:flex;align-items:center;gap:7px;font-size:16px;font-weight:600;color:#555}
.brand-dot{width:14px;height:14px;border-radius:50%;background:var(--green)}
.search{position:absolute;left:861px;top:12px;width:215px;height:42px;border-radius:21px;background:#f4f4f4;display:flex;align-items:center;padding-left:20px;gap:10px;font-size:12.5px;color:#bbb}
.hdr-icon{position:absolute;top:26px}
.sidebar{position:absolute;left:0;top:70px;width:227px;height:883px;background:var(--side)}
.profile{position:absolute;left:0;top:0;width:227px;height:186px;background:var(--side-top)}
.avatar{border-radius:50%;background:radial-gradient(circle at 50% 40%,#e8d2b8,#b99775)}
.greet{position:absolute;left:30px;top:114px;font-size:28px;font-weight:300;color:#555}
.greet b{color:var(--green);font-weight:700}
.greet-sub{position:absolute;left:30px;top:150px;font-size:12.5px;color:#666}
.nav-item{position:absolute;left:0;width:227px;height:30px;display:flex;align-items:center;font-size:12.5px;font-weight:600;color:#444}
.nav-item svg{position:absolute;left:35px}
.nav-item span{position:absolute;left:76px}
.nav-item.active{color:var(--green)}
.nav-item.active::before{content:"";position:absolute;left:0;top:4px;width:3px;height:22px;background:var(--green)}
.side-rule{position:absolute;left:28px;top:508px;width:138px;height:1px;background:#ddd}
.promo{position:absolute;left:30px;top:524px;font-size:16px;font-weight:300;line-height:19px;color:#444}
.btn-learn{position:absolute;left:27px;top:577px;width:119px;height:37px;border-radius:19px;background:var(--green);color:#fff;font-size:12px;font-weight:600;display:flex;align-items:center;justify-content:center;box-shadow:0 3px 6px rgba(140,198,63,.35)}
.nav-foot{color:#888;font-weight:400}
.main{position:absolute;left:227px;top:70px;width:713px;height:883px;background:var(--white)}
.scroll-track{position:absolute;left:925px;top:94px;width:4px;height:810px;background:#eee;border-radius:2px}
.scroll-thumb{position:absolute;left:925px;top:94px;width:4px;height:172px;background:#bbb;border-radius:2px}
.course-title{position:absolute;left:339px;top:101px;font-size:21px;font-weight:400;color:#444}
.author{position:absolute;left:340px;top:125px;font-size:12.5px;font-weight:700;color:#444}
.video{position:absolute;left:273px;top:164px;width:604px;height:373px;background:linear-gradient(135deg,#e6e2dc 0%,#cfc8bf 35%,#3a4a5c 60%,#1c232c 100%)}
.controls{position:absolute;left:0;bottom:0;width:604px;height:43px;background:rgba(10,10,10,.82);display:flex;align-items:center;color:#fff}
.progress{position:absolute;left:0;top:-2px;width:604px;height:3px;background:rgba(255,255,255,.35)}
.progress i{display:block;width:237px;height:3px;background:var(--green)}
.time{position:absolute;left:433px;font-size:12.5px}
.hd{position:absolute;left:507px;font-size:13px;font-weight:700}
.fav{position:absolute;left:273px;top:563px;width:92px;height:31px;border-radius:16px;background:#fff;box-shadow:0 2px 6px rgba(0,0,0,.1);display:flex;align-items:center;gap:8px;padding-left:13px;font-size:12px;color:var(--green)}
.share{position:absolute;left:379px;top:570px;display:flex;align-items:center;gap:9px;font-size:12px;font-weight:600;color:#555}
.stat{position:absolute;top:570px;display:flex;align-items:center;gap:8px;font-size:12px;font-weight:600;color:#555}
.rule{position:absolute;left:273px;top:632px;width:596px;height:1px;background:var(--line)}
.h-sec{position:absolute;top:663px;font-size:14px;font-weight:600;color:#444;letter-spacing:.2px}
.overview{position:absolute;left:283px;top:689px;width:375px;font-size:12.5px;line-height:14.7px;color:#777}
.duration{position:absolute;left:693px;top:690px;font-size:60px;font-weight:300;color:#777;line-height:1;letter-spacing:-2px}
.duration small{font-size:26px;letter-spacing:0;color:#999}
.chat{position:absolute;left:940px;top:70px;width:260px;height:883px;background:var(--white)}
.bubble{position:absolute;border-radius:5px;font-size:9.5px;line-height:11.6px;padding:0 14px}
.bubble.green{left:1002px;width:161px;background:var(--green);color:#fff;padding-top:9px}
.bubble.grey{left:1002px;width:161px;background:var(--bubble-grey);color:#555;padding-top:8px;padding-left:18px}
.bubble.short{left:1063px;width:100px;background:var(--bubble-grey);color:#555;padding-top:7px;padding-left:18px}
.chat-input{position:absolute;left:940px;top:875px;width:260px;height:78px;background:#f6f6f6}
.placeholder{position:absolute;left:967px;top:893px;font-size:9.5px;color:#bbb}
.send{position:absolute;left:1142px;top:893px;font-size:9.5px;font-weight:600;color:var(--green);display:flex;gap:5px;align-items:center}
</style>
</head>
<body>

<header class="header">
  <div class="brand"><span class="brand-dot"></span>CourseGrove</div>
  <div class="search">
    <svg width="13" height="13" viewBox="0 0 13 13"><circle cx="5.5" cy="5.5" r="4" fill="none" stroke="#bbb" stroke-width="2"/><path d="M8.5 8.5L12 12" stroke="#bbb" stroke-width="2"/></svg>
    Search
  </div>
  <svg class="hdr-icon" style="left:1114px;top:24px" width="18" height="20" viewBox="0 0 18 20"><path d="M2 15h12l-1.5-2V8a4.5 4.5 0 0 0-9 0v5z" fill="#c8c8c8"/><circle cx="8" cy="17" r="1.8" fill="#c8c8c8"/><circle cx="13" cy="4" r="4" fill="#e53935"/></svg>
  <svg class="hdr-icon" style="left:1140px;top:28px" width="17" height="13" viewBox="0 0 17 13"><rect width="17" height="13" rx="1.5" fill="#c8c8c8"/><path d="M1 1l7.5 6L16 1" fill="none" stroke="#fff" stroke-width="1.4"/></svg>
</header>

<aside class="sidebar">
  <div class="profile">
    <div class="avatar abs" role="img" aria-label="Student profile photo" style="left:27px;top:35px;width:66px;height:66px"></div>
  </div>
  <div class="greet">Hi, <b>Jane</b></div>
  <div class="greet-sub">What would you like to do?</div>

  <div class="nav-item" style="top:217px"><svg width="10" height="12" viewBox="0 0 10 12"><rect y="2" width="10" height="10" rx="1" fill="#444"/><rect x="3" width="4" height="3" fill="#444"/></svg><span>Dashboard</span></div>
  <div class="nav-item" style="top:270px"><svg width="12" height="9" viewBox="0 0 12 9"><rect width="12" height="9" rx="1" fill="#444"/><path d="M0.5 1l5.5 4 5.5-4" fill="none" stroke="#f8f8f8"/></svg><span>Messages</span></div>
  <div class="nav-item" style="top:322px"><svg width="14" height="10" viewBox="0 0 14 10"><rect width="14" height="10" rx="1" fill="#444"/><path d="M2 3h10M2 5h10M2 7h10" stroke="#f8f8f8"/></svg><span>Courses</span></div>
  <div class="nav-item active" style="top:375px"><svg width="10" height="12" viewBox="0 0 10 12"><path d="M0 0l10 6-10 6z" fill="#8cc63f"/></svg><span>Video Manager</span></div>
  <div class="nav-item" style="top:428px"><svg width="8" height="13" viewBox="0 0 8 13"><path d="M5 0L0 7h3l-1 6 6-8H5z" fill="#444"/></svg><span>Channels</span></div>

  <div class="side-rule"></div>
  <div class="promo">Chose the<br>best course for you</div>
  <div class="btn-learn">Learn More</div>

  <div class="nav-item nav-foot" style="top:762px"><svg width="12" height="12" viewBox="0 0 12 12"><circle cx="6" cy="6" r="4.5" fill="none" stroke="#999" stroke-width="3" stroke-dasharray="2 1.5"/><circle cx="6" cy="6" r="2" fill="#999"/></svg><span>Settings</span></div>
  <div class="nav-item nav-foot" style="top:815px"><svg width="12" height="10" viewBox="0 0 12 10"><path d="M5 1H1v8h4" fill="none" stroke="#999" stroke-width="1.6"/><path d="M4 5h6M8 2.5L10.5 5 8 7.5" fill="none" stroke="#999" stroke-width="1.6"/></svg><span>Log out</span></div>
</aside>

<main class="main"></main>
<div class="scroll-track"></div>
<div class="scroll-thumb"></div>

<div class="avatar abs" role="img" aria-label="Instructor photo" style="left:274px;top:98px;width:50px;height:50px;background:radial-gradient(circle at 50% 40%,#d9c1a6,#3c3f46)"></div>
<div class="course-title">Course Title</div>
<div class="author">Author Name</div>

<div class="video" role="img" aria-label="Lesson video: instructor presenting in a gallery room">
  <div class="controls">
    <div class="progress"><i></i></div>
    <svg class="abs" style="left:24px" width="9" height="11" viewBox="0 0 9 11"><path d="M0 0l9 5.5L0 11z" fill="#8cc63f"/></svg>
    <div class="abs" style="left:52px;width:76px;height:2px;background:#777"></div>
    <div class="abs" style="left:87px;width:9px;height:9px;border-radius:50%;background:#999"></div>
    <svg class="abs" style="left:145px" width="14" height="11" viewBox="0 0 14 11"><path d="M0 3.5h3L7 0v11L3 7.5H0z" fill="#fff"/><path d="M9 3q2 2.5 0 5M11 1.5q3.5 4 0 8" fill="none" stroke="#fff" stroke-width="1.3"/></svg>
    <span class="time">4:20/6:42</span>
    <span class="hd">HD</span>
    <svg class="abs" style="left:544px" width="12" height="12" viewBox="0 0 12 12"><circle cx="6" cy="6" r="4.3" fill="none" stroke="#fff" stroke-width="3" stroke-dasharray="2 1.4"/><circle cx="6" cy="6" r="1.6" fill="#fff"/></svg>
    <svg class="abs" style="left:564px" width="11" height="11" viewBox="0 0 11 11"><path d="M0 3.5V0h3.5M7.5 0H11v3.5M11 7.5V11H7.5M3.5 11H0V7.5" fill="none" stroke="#fff" stroke-width="1.6"/></svg>
  </div>
</div>

<div class="fav"><svg width="13" height="11" viewBox="0 0 13 11"><path d="M6.5 11L1 5.5A3 3 0 0 1 6.5 1.5 3 3 0 0 1 12 5.5z" fill="#8cc63f"/></svg>Favorite</div>
<div class="share"><svg width="11" height="11" viewBox="0 0 11 11"><circle cx="2" cy="5.5" r="2" fill="#555"/><circle cx="9" cy="2" r="2" fill="#555"/><circle cx="9" cy="9" r="2" fill="#555"/><path d="M2 5.5L9 2M2 5.5L9 9" stroke="#555" stroke-width="1.2"/></svg>Share</div>
<div class="stat" style="left:705px"><svg width="12" height="12" viewBox="0 0 12 12"><circle cx="6" cy="3.2" r="3" fill="#666"/><path d="M0 12q0-5 6-5t6 5z" fill="#666"/></svg>327</div>
<div class="stat" style="left:767px"><svg width="13" height="11" viewBox="0 0 13 11"><path d="M6.5 11L1 5.5A3 3 0 0 1 6.5 1.5 3 3 0 0 1 12 5.5z" fill="#666"/></svg>327</div>
<div class="stat" style="left:830px"><svg width="14" height="9" viewBox="0 0 14 9"><path d="M0 4.5Q7-4 14 4.5 7 13 0 4.5z" fill="#666"/><circle cx="7" cy="4.5" r="2" fill="#fff"/></svg>1.4k</div>

<div class="rule"></div>
<div class="h-sec" style="left:284px">Course Overview</div>
<p class="overview">Lorem ipsum dolor sit amet, consectetur adipisicing elit, sed do eiusmod tempor incididunt ut labore et dolore magna aliqua. Ut enim ad minim veniam, quis nostrud exercitation ullamco laboris nisi ut aliquip ex ea commodo consequat. Duis aute irure dolor in reprehenderit in voluptate velit esse cillum dolore eu fugiat nulla pariatur. Excepteur sint occaecat cupidatat non proident, sunt in culpa qui officia deserunt mollit anim id est laborum. Sed ut perspiciatis unde omnis iste natus error.</p>
<div class="h-sec" style="left:697px">Course Duration</div>
<div class="duration">46<small>mins</small></div>

<aside class="chat"></aside>
<div class="avatar abs" role="img" aria-label="Instructor photo" style="left:967px;top:103px;width:29px;height:29px;background:radial-gradient(circle at 50% 40%,#d9c1a6,#3c3f46)"></div>
<div class="bubble green" style="top:103px;height:57px">Lorem ipsum dolor sit amet, consectetur adipisicing elit, sed do eiusmod tempor</div>
<div class="bubble grey" style="top:174px;height:38px">Lorem ipsum dolor sit amet, consectetur</div>
<div class="bubble short" style="top:220px;height:26px">Lorem ipsum.</div>

<div class="avatar abs" role="img" aria-label="Instructor photo" style="left:967px;top:262px;width:29px;height:29px;background:radial-gradient(circle at 50% 40%,#d9c1a6,#3c3f46)"></div>
<div class="bubble green" style="top:262px;height:57px">Lorem ipsum dolor sit amet, consectetur adipisicing elit, sed do eiusmod tempor</div>
<div class="bubble green" style="top:324px;height:162px">Lorem ipsum dolor sit amet, consectetur adipisicing elit, sed do eiusmod tempor incididunt ut labore et dolore magna aliqua. Ut enim ad minim veniam, quis nostrud exercitation ullamco laboris nisi ut aliquip ex ea commodo consequat. Duis aute irure dolor in reprehenderit in voluptate velit esse cillum dolore eu fugiat nulla paria-</div>
<div class="bubble grey" style="top:500px;height:39px">Lorem ipsum dolor sit amet, consectetur</div>

<div class="avatar abs" role="img" aria-label="Instructor photo" style="left:967px;top:555px;width:29px;height:29px;background:radial-gradient(circle at 50% 40%,#d9c1a6,#3c3f46)"></div>
<div class="bubble green" style="top:555px;height:57px">Lorem ipsum dolor sit amet, consectetur adipisicing elit, sed do eiusmod tempor</div>
<div class="bubble grey" style="top:626px;height:39px">Lorem ipsum dolor sit amet, consectetur</div>
<div class="bubble short" style="top:671px;height:27px">Lorem ipsum.</div>

<div class="chat-input"></div>
<div class="placeholder">Start typing a massage...</div>
<div class="send">Send <svg width="11" height="10" viewBox="0 0 11 10"><path d="M0 4.5L11 0 8 10 5.5 6z" fill="#8cc63f"/></svg></div>

</body>
</html>
```